Business card design needed for Automotive Reconditioning business

I have a logo design i just cant decide on the best color or layout for the business card, I will upload all the files so you can see all colors schemes we are considering. I have other file formats if needed let me know.

Target Market(s)

automotive dealerships

Contact Information for Business Card

HERE are the Descriptions and info needed on the card:
Interior Repair: Leather carpet burns panels dash Deoderize
Dealer products and Vin Verify
( spot for name and cell number) My name is Norman Bexley phone 614 352-4180 Title COO www.QuorvalMotive.com

Font styles to use
Sans Serif
Other font styles liked:
• what ever you think looks best

Requirements
Must have
• Must be able to change the name and phone for employees

```html
<!DOCTYPE html>
<html lang="en">
<head>
<meta charset="utf-8">
<title>Quorval Auto Reconditioning Corp. – Business Card</title>
<link href="https://fonts.googleapis.com/css2?family=Outfit:wght@600;700&family=Roboto:wght@700&family=Teko:wght@500&display=swap" rel="stylesheet">
<style>
  :root {
    --page: #ffffff;
    --card-dark: #333333;
    --white: #ffffff;
    --orange: #f5841f;
    --red: #ed2229;
  }
  html, body {
    margin: 0;
    width: 1200px;
    height: 1200px;
    overflow: hidden;
    background: var(--page);
  }
  .canvas {
    position: relative;
    width: 1200px;
    height: 1200px;
  }
  .card {
    position: absolute;
    left: 100px;
    top: 320px;
    width: 1000px;
    height: 560px;
    background: var(--card-dark);
    overflow: hidden;
    color: var(--white);
  }
  .accent-band {
    position: absolute;
    inset: 0;
  }
  .services {
    position: absolute;
    left: 48px;
    top: 88px;
    margin: 0;
    font-family: "Outfit", sans-serif;
    font-weight: 700;
    font-size: 34px;
    line-height: 44px;
    letter-spacing: 0.5px;
    text-transform: uppercase;
  }
  .services span { display: block; }
  .tagline {
    position: absolute;
    left: 600px;
    top: 30px;
    font-family: "Teko", sans-serif;
    font-weight: 500;
    font-style: italic;
    font-size: 48px;
    line-height: 38px;
    text-transform: uppercase;
  }
  .tagline .line-two { padding-left: 142px; }
  .contact {
    position: absolute;
    left: 590px;
    top: 108px;
  }
  .phone {
    display: flex;
    align-items: center;
    gap: 12px;
    font-family: "Roboto", sans-serif;
    font-weight: 700;
    font-size: 42px;
    letter-spacing: 0.5px;
  }
  .phone-icon { width: 52px; height: 52px; }
  .website {
    margin-top: 4px;
    margin-left: 6px;
    font-family: "Outfit", sans-serif;
    font-weight: 600;
    font-size: 28px;
    letter-spacing: 1px;
  }
  .person {
    position: absolute;
    left: 611px;
    top: 268px;
    width: 300px;
    text-align: center;
    font-family: "Outfit", sans-serif;
    font-weight: 600;
    font-size: 27px;
    line-height: 34px;
    text-transform: uppercase;
  }
  .person .name {
    display: inline-block;
    border-bottom: 2px solid var(--white);
    line-height: 28px;
    white-space: nowrap;
  }
  .brand-name {
    position: absolute;
    left: 94px;
    top: 456px;
    margin: 0;
    font-family: "Outfit", sans-serif;
    font-weight: 700;
    color: var(--white);
    text-transform: uppercase;
    line-height: 1;
  }
  .brand-name .main { display: block; font-size: 52px; letter-spacing: 7px; }
  .brand-name .sub { display: block; font-size: 25px; margin-top: 6px; letter-spacing: 0.5px; }
</style>
</head>
<body>
<div class="canvas">
  <section class="card">
    <svg class="accent-band" viewBox="0 0 1000 560" preserveAspectRatio="none" role="img" aria-label="Decorative orange to red band along the lower edge of the card">
      <defs>
        <linearGradient id="band-fill" x1="0" y1="0" x2="0" y2="1">
          <stop offset="0" stop-color="var(--orange)"/>
          <stop offset="0.45" stop-color="var(--red)"/>
          <stop offset="1" stop-color="var(--red)"/>
        </linearGradient>
      </defs>
      <path fill="url(#band-fill)" d="M0,330 C150,290 300,272 420,318 C520,365 560,455 700,458 C820,460 900,362 1000,305 L1000,560 L0,560 Z"/>
    </svg>

    <p class="services">
      <span>Interior Repair:</span>
      <span>Leather Carpet</span>
      <span>Burns Panels Dash</span>
      <span>Deoderize</span>
    </p>

    <div class="tagline">
      <div>Dealer Products</div>
      <div class="line-two">&amp; VIN Verify</div>
    </div>

    <div class="contact">
      <div class="phone">
        <svg class="phone-icon" viewBox="0 0 52 52" aria-hidden="true">
          <circle cx="26" cy="26" r="25" fill="var(--white)"/>
          <path fill="var(--card-dark)" d="M18.5,12.5c1.2-0.8,2.6-0.5,3.4,0.7l3,4.6c0.7,1.1,0.5,2.5-0.5,3.3l-2.2,1.8c1.4,3.3,3.8,6,7,7.6l1.9-2.1c0.9-1,2.3-1.1,3.4-0.4l4.5,3.1c1.1,0.8,1.4,2.3,0.6,3.4l-1.9,2.7c-1,1.4-2.8,2-4.4,1.5C23.9,35.8,16.3,28,13.6,18.5c-0.4-1.6,0.2-3.3,1.6-4.2Z"/>
        </svg>
        <span>614 352-4180</span>
      </div>
      <div class="website">www.QuorvalMotive.com</div>
    </div>

    <div class="person">
      <span class="name">Norman Bexley</span><br>
      <span class="title">COO</span>
    </div>

    <h1 class="brand-name">
      <span class="main">Quorval</span>
      <span class="sub">Auto Reconditioning Corp.</span>
    </h1>
  </section>
</div>
</body>
</html>
```